Educational Textbook Covern Design for mostly females

Create a textbook cover (will be white spiral) using the Brandguide.pdf attached. This will be a textbook given to mostly age 18-25 year old women so a modern trendy cute type design is wanted.
The book cover is 8.5" x 11" which will be printed in CMYK full bleed.
The name "LoriPQX's Dental Hygiene Academy" must be on the cover somewhere and "LoriPQX" has to be either the same height or larger height than the "Dental Hygiene Academy"

Please no real life photos such as images of dentists, etc. This should be all created art.

The year "2025" should be in the design as well.

IMPORTANT UPDATED 8/4/2024
These designs should not look too childish. This should be a professional textbook for dental professionals. All the current designs have too much cartoon art.

Target Market(s)

18-25 year old females

Industry/Entity Type

Dentistry

Font styles to use
Other font styles liked:
• See brand guide

Colors
A7469A
B969AE
D3A5CF
EDDBEB
F8F0F9
6B429C
8869AF
B7A5CE
E3DAEB
F3F0F8

Requirements
Should not have
• No photos, should be all art

```html
<!DOCTYPE html>
<html lang="en">
<head>
<meta charset="utf-8">
<title>LoriPQX's Dental Hygiene Academy 2025 Textbook Cover</title>
<link rel="stylesheet" href="https://fonts.googleapis.com/css2?family=Fredoka:wght@700&family=Quicksand:wght@500;600&display=swap">
<style>
  :root {
    --page: #ffffff;
    --ink-light: #ffffff;
    --deep-blue: #0f4f9a;
    --blue: #1d5f8a;
    --teal: #1f6e66;
    --leaf: #5b9245;
    --moss: #8fa53a;
    --sun: #eee716;
    --lemon: #e6d51f;
    --gold: #e8bf22;
    --amber: #eea326;
    --orange: #e7862b;
    --forest: #1f5e31;
    --bark: #4a4a26;
  }
  * { margin: 0; padding: 0; box-sizing: border-box; }
  html, body {
    width: 1200px;
    height: 1200px;
    overflow: hidden;
    background: var(--page);
  }
  .canvas {
    position: relative;
    width: 1200px;
    height: 1200px;
    background: var(--page);
  }
  .cover {
    position: absolute;
    left: 182px;
    top: 60px;
    width: 834px;
    height: 1078px;
    overflow: hidden;
  }
  .cover-art {
    position: absolute;
    inset: 0;
    background:
      radial-gradient(ellipse 26% 24% at 58% 56%, var(--sun) 0%, rgba(238,231,22,0) 100%),
      radial-gradient(ellipse 34% 14% at 68% 100%, var(--orange) 0%, rgba(231,134,43,0) 100%),
      radial-gradient(ellipse 30% 22% at 60% 88%, var(--amber) 0%, rgba(238,163,38,0) 100%),
      radial-gradient(ellipse 22% 12% at 40% 2%, var(--amber) 0%, rgba(238,163,38,0) 100%),
      radial-gradient(ellipse 34% 46% at 57% 50%, var(--lemon) 0%, rgba(230,213,31,0) 100%),
      radial-gradient(ellipse 42% 62% at 55% 48%, var(--gold) 0%, rgba(232,191,34,0) 100%),
      radial-gradient(ellipse 16% 14% at 100% 96%, var(--bark) 0%, rgba(74,74,38,0) 100%),
      linear-gradient(90deg, var(--deep-blue) 0%, var(--blue) 6%, var(--teal) 16%, var(--leaf) 30%, var(--moss) 48%, var(--moss) 62%, var(--leaf) 80%, var(--forest) 100%);
  }
  .masthead {
    position: absolute;
    left: 0;
    top: 0;
    width: 100%;
    height: 200px;
    color: var(--ink-light);
  }
  .brand-name {
    position: absolute;
    left: 326px;
    top: 36px;
    font-family: "Fredoka", sans-serif;
    font-weight: 700;
    font-size: 58px;
    line-height: 1;
    letter-spacing: 0.5px;
    white-space: nowrap;
  }
  .brand-tagline {
    position: absolute;
    left: 365px;
    top: 92px;
    font-family: "Quicksand", sans-serif;
    font-weight: 600;
    font-size: 17px;
    line-height: 1;
    letter-spacing: 0.4px;
    white-space: nowrap;
  }
  .masthead-divider {
    position: absolute;
    left: 660px;
    top: 37px;
    width: 2px;
    height: 78px;
    background: var(--ink-light);
  }
  .edition-year {
    position: absolute;
    left: 675px;
    top: 37px;
    font-family: "Quicksand", sans-serif;
    font-weight: 500;
    font-size: 52px;
    line-height: 1;
    letter-spacing: 1px;
  }
</style>
</head>
<body>
  <main class="canvas">
    <section class="cover">
      <div class="cover-art" role="img" aria-label="Low-poly triangular mosaic background blending blue and green at the edges into a bright yellow centre and warm orange at the bottom"></div>
      <header class="masthead">
        <h1 class="brand-name">LORIPQX'S</h1>
        <p class="brand-tagline">Dental Hygiene Academy</p>
        <span class="masthead-divider"></span>
        <p class="edition-year">2025</p>
      </header>
    </section>
  </main>
</body>
</html>
```